Book Cover Design 'Boundless Tide - Lessons In Inner Sovereignty'

I need to see pitches / artwork for a book cover for new book designed to start a new global spiritual movement and save humanity. The book merges science and spirituality and explains to the reader why they are an all powerful god.

```html
<!DOCTYPE html>
<html lang="en">
<head>
<meta charset="utf-8">
<title>Boundless Tide – Book Cover</title>
<link rel="stylesheet" href="https://fonts.googleapis.com/css2?family=Montserrat:wght@300;400;600;700;800&family=Open+Sans:wght@400;600&display=swap">
<style>
  :root {
    --page-bg: #9b9b9b;
    --spine: #2b2a5e;
    --title-gold: #f6c400;
    --ink-light: #ffffff;
    --sky-top: #16153f;
    --sky-mid: #3c3b7e;
    --sky-glow: #7a72a8;
    --horizon: #d7b2c9;
    --ground: #0e0d16;
  }
  * { box-sizing: border-box; margin: 0; padding: 0; }
  html, body {
    width: 793px; height: 1200px; overflow: hidden;
    background: var(--page-bg);
  }
  .cover-spread {
    position: absolute;
    left: 20px; top: 334px;
    width: 754px; height: 532px;
    display: flex;
  }
  .back-cover, .front-cover { position: relative; width: 356px; height: 532px; overflow: hidden; }
  .spine { width: 42px; height: 532px; background: var(--spine); position: relative; }

  .night-sky {
    position: absolute; inset: 0;
    background:
      radial-gradient(ellipse 60% 35% at 78% 12%, rgba(170,110,200,.55), transparent 70%),
      radial-gradient(ellipse 55% 30% at 50% 86%, var(--horizon), transparent 75%),
      linear-gradient(155deg, var(--sky-top) 0%, var(--sky-mid) 40%, var(--sky-glow) 70%, #5c5478 86%, var(--ground) 93%);
  }
  .back-cover .night-sky::after {
    content: ""; position: absolute; inset: 0;
    background: rgba(200,200,215,.32);
  }

  .back-copy {
    position: absolute; left: 45px; width: 266px;
    font-family: "Open Sans", sans-serif; color: var(--ink-light);
  }
  .back-copy h2 {
    font-weight: 400; font-size: 8.5px; text-align: center; margin-bottom: 6px;
  }
  .back-copy p {
    font-size: 5.6px; line-height: 7.4px; text-align: justify; margin-bottom: 9px;
  }
  .synopsis { top: 36px; }
  .author-bio { top: 141px; }
  .testimonials { top: 319px; }

  .spine-text {
    position: absolute; left: 50%; top: 50%;
    transform: translate(-50%, -50%) rotate(-90deg);
    white-space: nowrap;
    font-family: "Montserrat", sans-serif; font-weight: 400;
    font-size: 15px; letter-spacing: 3px; color: var(--ink-light);
  }
  .spine-text .divider { margin: 0 14px; font-weight: 300; }
  .spine-text .spine-author { letter-spacing: 5px; }

  .front-titles {
    position: absolute; top: 30px; left: 0; width: 100%;
    text-align: center; font-family: "Montserrat", sans-serif; color: var(--ink-light);
  }
  .book-title {
    font-weight: 700; font-size: 31px; line-height: 34px;
    color: var(--title-gold); letter-spacing: .3px;
  }
  .book-subtitle {
    font-weight: 300; font-size: 16px; margin-top: 2px; letter-spacing: .3px;
  }
  .book-author {
    font-weight: 700; font-size: 21px; margin-top: 14px;
  }
</style>
</head>
<body>
  <main class="cover-spread">
    <section class="back-cover">
      <div class="night-sky" role="img" aria-label="Starry night sky with the Milky Way above a silhouetted person meditating on a hilltop among trees"></div>
      <div class="back-copy synopsis">
        <h2>Short Synopsis</h2>
        <p>Boundless Tide bridges modern physics and ancient contemplative wisdom to reveal a simple, startling truth: the awareness reading these words is the same awareness that shapes the cosmos. Through clear reasoning, guided practice and gentle provocation, this book invites you to drop the story of smallness and step into your full creative power. It is a handbook for a quieter mind, a braver heart and a kinder world.</p>
      </div>
      <div class="back-copy author-bio">
        <h2>Author Bio</h2>
        <p>Elias Marren is a teacher, researcher and lifelong student of consciousness. After two decades exploring the overlap between quantum theory, neuroscience and the world's meditative traditions, he began guiding retreats that blend rigorous inquiry with deep stillness. His work has reached seekers on every continent, and his talks are known for their warmth, humour and uncompromising honesty about what it means to be fully awake.</p>
        <p>He lives by the sea with his family, where he writes at dawn, walks the shoreline at dusk and still finds the night sky the finest classroom he has ever known. Boundless Tide is the distillation of everything those years have taught him, offered freely to anyone ready to remember who they truly are and to live from that remembering every day.</p>
      </div>
      <div class="back-copy testimonials">
        <h2>Testimonials</h2>
        <p>“A rare book that speaks to both the scientist and the mystic in each of us. I finished it changed.” — Dr. Lena Ashby. “Clear, daring and deeply compassionate. Marren hands you the keys and trusts you to open the door yourself.” — Tomas Reyes. “Read it slowly, then read it again. Every page widens the horizon of what you believe is possible.” — Amara Quinn</p>
      </div>
    </section>

    <section class="spine">
      <div class="spine-text">BOUNDLESS TIDE<span class="divider">|</span><span class="spine-author">Elias Marren</span></div>
    </section>

    <section class="front-cover">
      <div class="night-sky" role="img" aria-label="Starry night sky with the Milky Way above a silhouetted person meditating on a hilltop among trees"></div>
      <div class="front-titles">
        <h1 class="book-title">BOUNDLESS TIDE</h1>
        <p class="book-subtitle">Lessons In Inner Sovereignty</p>
        <p class="book-author">Elias Marren</p>
      </div>
    </section>
  </main>
</body>
</html>
```